Business Card Design Project

We need a business card design for an existing company in Dallas/Fort Worth that is expanding services and re-branding. We are changing the name from Brightmoor Commercial Cleaning to Keystride Facility Services. We are expanding from only commercial cleaning to include complete commercial landscape and facility maintenance services, too.

As stated, we offer a package of services that includes landscape, janitorial and facility services, which is largely unique in the industry.

We would like a design that communicates trust/partnership with a professional, corporate image, but not necessarily using the standard white business card. We would like a design that perhaps uses darker blues or perhaps a gray background, but we are open to other ideas. We might also be interested in a double-sided design - maybe with our logo on the back, printed on a gray background?

We will probably stick with the attached logo, but if you've got another inspired idea....

Target Market(s)

Property managers, commercial real estate professionals, corporate executives

Industry/Entity Type

Landscape

Requirements
Should not have
• Not interested in old style fonts.

```html
<!DOCTYPE html>
<html lang="en">
<head>
<meta charset="utf-8">
<title>Keystride Facility Services – Business Card</title>
<link rel="stylesheet" href="https://fonts.googleapis.com/css2?family=Roboto+Condensed:wght@700&family=Roboto:wght@300;700&family=Archivo+Black&display=swap">
<style>
  :root {
    --bg-light: #e6e6e6;
    --bg-mid: #d2d2d2;
    --bg-dark: #b9b9b9;
    --blue-1: #0f6fa8;
    --blue-2: #2a8cc4;
    --blue-3: #7aa9c2;
    --grey-band-1: #7c7c7c;
    --grey-band-2: #a8a8a8;
    --ink: #111111;
    --subtle-ink: #4a4a4a;
    --contact-ink: #333333;
    --label-ink: #ffffff;
    --ghost: rgba(255, 255, 255, 0.42);
  }
  html, body {
    margin: 0;
    padding: 0;
    width: 1200px;
    height: 686px;
    overflow: hidden;
    background: #ffffff;
  }
  .card {
    position: relative;
    width: 1200px;
    height: 686px;
    overflow: hidden;
    background: radial-gradient(ellipse at 40% 45%, var(--bg-light) 0%, var(--bg-mid) 60%, var(--bg-dark) 100%);
    font-family: "Roboto", Arial, sans-serif;
  }
  .top-band, .bottom-band {
    position: absolute;
    left: 0;
    width: 1200px;
    display: flex;
  }
  .top-band { top: 0; height: 37px; }
  .bottom-band { bottom: 0; height: 19px; }
  .top-band span, .bottom-band span { flex: 1; }
  .top-band span:nth-child(1) { background: #0f6aa3; }
  .top-band span:nth-child(2) { background: #1b79b0; }
  .top-band span:nth-child(3) { background: #2686bb; }
  .top-band span:nth-child(4) { background: #2a8fc3; }
  .top-band span:nth-child(5) { background: #2a96c8; }
  .top-band span:nth-child(6) { background: #3c9ac8; }
  .top-band span:nth-child(7) { background: #55a2c6; }
  .top-band span:nth-child(8) { background: #6ba6c3; }
  .top-band span:nth-child(9) { background: #7aa9c0; }
  .bottom-band span:nth-child(odd) { background: var(--grey-band-1); }
  .bottom-band span:nth-child(even) { background: var(--grey-band-2); }
  .tile-grid {
    position: absolute;
    top: 37px;
    right: 0;
    width: 400px;
    height: 290px;
  }
  .ghost-word {
    position: absolute;
    left: 2px;
    top: 130px;
    margin: 0;
    font-family: "Archivo Black", Arial, sans-serif;
    font-size: 218px;
    line-height: 1;
    letter-spacing: 2px;
    color: var(--ghost);
    white-space: nowrap;
  }
  .partnership-art {
    position: absolute;
    left: 60px;
    top: 385px;
    width: 420px;
    height: 215px;
    border-radius: 24px;
    background: linear-gradient(135deg, rgba(255,255,255,0.30), rgba(255,255,255,0.12));
  }
  .company-name {
    position: absolute;
    left: 176px;
    top: 246px;
    margin: 0;
    font-family: "Roboto Condensed", "Arial Narrow", sans-serif;
    font-weight: 700;
    font-size: 96px;
    line-height: 1;
    letter-spacing: -2px;
    color: var(--ink);
    white-space: nowrap;
  }
  .name-rule {
    position: absolute;
    left: 150px;
    top: 344px;
    width: 900px;
    height: 10px;
    background: radial-gradient(ellipse at 50% 0%, rgba(0,0,0,0.28) 0%, rgba(0,0,0,0) 70%);
  }
  .holder {
    position: absolute;
    right: 166px;
    top: 354px;
    margin: 0;
    font-family: "Roboto", Arial, sans-serif;
    font-weight: 300;
    font-size: 33px;
    color: var(--subtle-ink);
    white-space: nowrap;
  }
  .contact {
    position: absolute;
    left: 600px;
    top: 527px;
    margin: 0;
    display: grid;
    grid-template-columns: 147px auto;
    row-gap: 6px;
    font-size: 25px;
    line-height: 25px;
  }
  .contact dt {
    text-align: right;
    font-weight: 700;
    color: var(--label-ink);
    padding-right: 26px;
    position: relative;
  }
  .contact dt::after {
    content: "·";
    position: absolute;
    right: 8px;
    color: var(--label-ink);
  }
  .contact dd {
    margin: 0;
    color: var(--contact-ink);
    font-weight: 300;
    white-space: nowrap;
  }
</style>
</head>
<body>
  <main class="card">
    <div class="top-band"><span></span><span></span><span></span><span></span><span></span><span></span><span></span><span></span><span></span></div>

    <svg class="tile-grid" viewBox="0 0 400 290" aria-hidden="true">
      <rect x="0" y="0" width="130" height="80" fill="#ffffff" opacity="0.12"/>
      <rect x="130" y="0" width="135" height="80" fill="#9a9a9a" opacity="0.18"/>
      <rect x="265" y="0" width="135" height="80" fill="#8c8c8c" opacity="0.25"/>
      <rect x="130" y="80" width="135" height="90" fill="#ffffff" opacity="0.10"/>
      <rect x="265" y="80" width="135" height="90" fill="#a0a0a0" opacity="0.20"/>
      <rect x="265" y="170" width="135" height="120" fill="#ffffff" opacity="0.10"/>
    </svg>

    <p class="ghost-word" aria-hidden="true">Keystride</p>

    <div class="partnership-art" role="img" aria-label="Faint handshake symbol suggesting partnership"></div>

    <h1 class="company-name">Keystride Facility Services</h1>
    <div class="name-rule" aria-hidden="true"></div>
    <p class="holder">Reid Calloway. General Manager</p>

    <dl class="contact">
      <dt>website</dt><dd>www.keystridefacilityservices.com</dd>
      <dt>email</dt><dd>hello@keystride.com</dd>
      <dt>phone</dt><dd>555.214.0387</dd>
    </dl>

    <div class="bottom-band"><span></span><span></span><span></span><span></span><span></span><span></span><span></span><span></span><span></span></div>
  </main>
</body>
</html>
```